Business Card Design

I want a non fussy clear design. I like Vintage, Retro writing for the main name as it will be a banner for the roof sign.
Company name, address and ph no. I would also like a unisex symbol small in the corner of the card. The colour of the card does not have to be blue. But I do want a bright clean clear card. A head sillohette small in the other corner possibly.

Industry/Entity Type

Business

Contact Information for Business Card

Zet Hair Design
318 Kellaby Road, Kellaby
Ph (09) 4162903

Requirements
Must have
• The back of the card must have appointment time, date dont worry about the location as its obviously on the front of the card

```html
<!DOCTYPE html>
<html lang="en">
<head>
<meta charset="utf-8">
<title>Zet Hair Design – Business Card</title>
<link rel="stylesheet" href="https://fonts.googleapis.com/css2?family=Poiret+One&family=Questrial&family=Mulish:wght@700&family=Kaushan+Script&display=swap">
<style>
  :root {
    --backdrop: #000000;
    --brand-blue: #0070b8;
    --card-white: #ffffff;
    --ink-white: #ffffff;
    --hair-tone: #e9eef4;
  }
  * { margin: 0; padding: 0; box-sizing: border-box; }
  html, body {
    width: 1097px;
    height: 1200px;
    overflow: hidden;
    background: var(--backdrop);
  }
  .canvas {
    position: relative;
    width: 1097px;
    height: 1200px;
  }

  /* Front of card */
  .card-front {
    position: absolute;
    left: 75px;
    top: 75px;
    width: 650px;
    height: 396px;
    background: var(--brand-blue);
    color: var(--ink-white);
  }
  .business-name {
    position: absolute;
    top: 118px;
    left: 0;
    width: 100%;
    text-align: center;
    font-family: "Poiret One", sans-serif;
    font-size: 74px;
    letter-spacing: 1px;
    line-height: 1;
    text-transform: uppercase;
    text-shadow: 2px 3px 2px rgba(0,0,0,0.35);
  }
  .contact {
    position: absolute;
    top: 212px;
    left: 0;
    width: 100%;
    text-align: center;
    font-family: "Questrial", sans-serif;
    font-size: 23px;
    line-height: 1.25;
  }
  .contact-line {
    display: flex;
    justify-content: center;
    align-items: center;
    gap: 6px;
  }
  .contact-icon {
    width: 20px;
    height: 20px;
    fill: var(--ink-white);
  }
  .hair-silhouette {
    position: absolute;
    left: 26px;
    bottom: 26px;
    width: 96px;
    height: 92px;
    border-radius: 46% 46% 38% 38%;
    background: radial-gradient(circle at 45% 40%, var(--hair-tone), #c9d6e4);
  }
  .unisex-symbol {
    position: absolute;
    right: 36px;
    bottom: 34px;
    width: 58px;
    height: 90px;
  }

  /* Back of card */
  .card-back {
    position: absolute;
    left: 530px;
    top: 500px;
    width: 400px;
    height: 660px;
    background: var(--card-white);
    color: var(--brand-blue);
    font-family: "Mulish", sans-serif;
    font-weight: 700;
    text-align: center;
  }
  .back-heading {
    position: absolute;
    top: 58px;
    width: 100%;
    font-size: 22px;
  }
  .fill-line {
    position: absolute;
    left: 50%;
    height: 2px;
    background: var(--brand-blue);
    transform: translateX(-50%);
  }
  .fill-line--name { top: 150px; width: 224px; }
  .fill-line--date { top: 288px; width: 150px; }
  .fill-line--time { top: 390px; width: 108px; }
  .back-label {
    position: absolute;
    width: 100%;
    font-size: 22px;
  }
  .back-label--is-on { top: 200px; }
  .time-colon { top: 356px; font-size: 18px; }
  .back-label--ampm { top: 398px; word-spacing: 6px; }
  .sign-off {
    position: absolute;
    top: 540px;
    width: 100%;
    font-family: "Kaushan Script", cursive;
    font-weight: 400;
    font-size: 34px;
    line-height: 1.55;
  }
</style>
</head>
<body>
<main class="canvas">

  <section class="card-front" aria-label="Card front">
    <h1 class="business-name">Zet Hair Design</h1>
    <div class="contact">
      <p class="contact-line">
        <svg class="contact-icon" viewBox="0 0 20 20" aria-hidden="true">
          <path d="M10 2 L1 10 H4 V18 H8 V13 H12 V18 H16 V10 H19 Z"/>
        </svg>
        318 Kellaby Road, Kellaby
      </p>
      <p class="contact-line">
        <svg class="contact-icon" viewBox="0 0 20 20" aria-hidden="true">
          <path d="M5 2 L8 2 L9 6 L7 8 C8 11 9 12 12 13 L14 11 L18 12 L18 15 C18 17 16 18 14 18 C8 17 3 12 2 6 C2 4 3 2 5 2 Z"/>
        </svg>
        (09) 4162903
      </p>
    </div>
    <div class="hair-silhouette" role="img" aria-label="Small white silhouette of flowing hair"></div>
    <svg class="unisex-symbol" viewBox="0 0 58 90" role="img" aria-label="Unisex symbol">
      <g fill="none" stroke="var(--ink-white)" stroke-width="6" stroke-linecap="square">
        <circle cx="24" cy="38" r="16"/>
        <line x1="24" y1="54" x2="24" y2="84"/>
        <line x1="12" y1="72" x2="36" y2="72"/>
        <line x1="35" y1="27" x2="52" y2="8"/>
        <polyline points="38,6 53,6 53,21"/>
      </g>
    </svg>
  </section>

  <section class="card-back" aria-label="Card back">
    <p class="back-heading">Your next appointment with</p>
    <span class="fill-line fill-line--name"></span>
    <p class="back-label back-label--is-on">is on</p>
    <span class="fill-line fill-line--date"></span>
    <p class="back-label time-colon">:</p>
    <span class="fill-line fill-line--time"></span>
    <p class="back-label back-label--ampm">am pm</p>
    <p class="sign-off">We look forward<br>to seeing you soon!</p>
  </section>

</main>
</body>
</html>
```